Need a business card design for a residential architect.

You can get a sense of his work at www.tbrolvik.com

Would like a consistent look and feel between business card and website
.

Target Market(s)

Residential homeowners builders

Industry/Entity Type

Residential

Contact Information for Business Card

Dale Brolvik
Principle
Brolvik Architecture
418 Quill Lane
Menlo Park, CA 94025

dale@tbrolvik.com

tbrolvik.com
phone: 650-555-0172
Fax: 650-555-0196

Font styles to use
Sans Serif

Requirements
Must have
• Details above
Nice to have
• Would like a consistent look and feel between business card and website
Should not have
• None

```html
<!DOCTYPE html>
<html lang="en">
<head>
<meta charset="utf-8">
<title>Brolvik Architecture – Business Card</title>
<link rel="stylesheet" href="https://fonts.googleapis.com/css2?family=Arimo:wght@400;700&display=swap">
<style>
  :root {
    --page-bg: #e4e4e4;
    --card-white: #ffffff;
    --band-black: #161616;
    --ink-dark: #111111;
    --ink-brand-grey: #6d6d6d;
    --ink-contact: #8c8c8c;
    --icon-grey: #8a8a8a;
    --photo-deep: #46562f;
    --photo-light: #7a9458;
  }
  * { box-sizing: border-box; margin: 0; padding: 0; }
  html, body {
    width: 992px;
    height: 1200px;
    overflow: hidden;
    background: var(--page-bg);
    font-family: "Arimo", Arial, sans-serif;
  }
  .card {
    position: absolute;
    left: 76px;
    width: 870px;
    height: 495px;
    border-radius: 20px;
    overflow: hidden;
  }

  /* Front */
  .card--front {
    top: 67px;
    background: var(--card-white);
  }
  .holder {
    position: absolute;
    left: 71px;
    top: 82px;
    color: var(--ink-dark);
  }
  .holder__name {
    font-size: 22px;
    font-weight: 700;
    line-height: 1;
  }
  .holder__title {
    font-size: 16px;
    font-weight: 400;
    margin-top: 10px;
  }
  .brand-name {
    position: absolute;
    font-weight: 400;
    line-height: 1;
    white-space: nowrap;
  }
  .card--front .brand-name {
    right: 43px;
    top: 118px;
    font-size: 38px;
    color: var(--ink-brand-grey);
  }
  .contact-band {
    position: absolute;
    left: 0;
    top: 290px;
    width: 100%;
    height: 186px;
    background: var(--band-black);
  }
  .contact {
    position: absolute;
    left: 60px;
    display: flex;
    align-items: center;
    gap: 28px;
    font-size: 17px;
    line-height: 20px;
    color: var(--ink-contact);
  }
  .contact svg {
    width: 20px;
    height: 20px;
    fill: var(--icon-grey);
    flex: none;
  }
  .contact--address { top: 14px; }
  .contact--phone   { top: 54px; }
  .contact--fax     { top: 85px; }
  .contact--email   { top: 123px; }
  .contact--web     { top: 151px; }

  /* Back */
  .card--back {
    top: 627px;
  }
  .card__photo {
    position: absolute;
    inset: 0;
    background: linear-gradient(160deg, var(--photo-deep) 0%, var(--photo-light) 100%);
  }
  .card--back .brand-name {
    left: 64px;
    top: 388px;
    font-size: 46px;
    color: var(--ink-dark);
  }
</style>
</head>
<body>

<section class="card card--front" aria-label="Business card front">
  <div class="holder">
    <p class="holder__name">Dale Brolvik</p>
    <p class="holder__title">Principle</p>
  </div>

  <p class="brand-name">Brolvik Architecture</p>

  <div class="contact-band">
    <p class="contact contact--address">
      <svg viewBox="0 0 24 24" aria-hidden="true"><path d="M12 2a7 7 0 0 0-7 7c0 5.2 7 13 7 13s7-7.8 7-13a7 7 0 0 0-7-7zm0 9.5A2.5 2.5 0 1 1 12 6.5a2.5 2.5 0 0 1 0 5z"/></svg>
      418 Quill Lane Menlo Park, CA 94025
    </p>
    <p class="contact contact--phone">
      <svg viewBox="0 0 24 24" aria-hidden="true"><path d="M3 8c0-2 4-4 9-4s9 2 9 4v2h-4V8.5c-1.5-.6-3-.8-5-.8s-3.5.2-5 .8V10H3zM6 12l2-3h8l2 3v7H6zm6 1.5a2 2 0 1 0 0 4 2 2 0 0 0 0-4z"/></svg>
      650-555-0172
    </p>
    <p class="contact contact--fax">
      <svg viewBox="0 0 24 24" aria-hidden="true"><path d="M7 3h10v4H7zM4 8h16a2 2 0 0 1 2 2v6h-4v-3H6v3H2v-6a2 2 0 0 1 2-2zm3 6h10v6H7z"/></svg>
      650-555-0196
    </p>
    <p class="contact contact--email">
      <svg viewBox="0 0 24 24" aria-hidden="true"><path d="M2 5h20v14H2zm2 2v.5l8 5.5 8-5.5V7zm0 2.9V17h16V9.9l-8 5.5z"/></svg>
      dale@tbrolvik.com
    </p>
    <p class="contact contact--web">
      <svg viewBox="0 0 24 24" aria-hidden="true"><path d="M2 3h20v14H2zm2 2v10h16V5zM9 18h6v2h3v1H6v-1h3z"/></svg>
      tbrolvik.com
    </p>
  </div>
</section>

<section class="card card--back" aria-label="Business card back">
  <div class="card__photo" role="img" aria-label="Photograph of a residential cottage with garden, lawn and swimming pool"></div>
  <p class="brand-name">Brolvik Architecture</p>
</section>

</body>
</html>
```